Homes, Invest in Non-performing loans

We need only 3 web pages, one for the home, one for the content, one for the properties.
The main focus of our business is to offer non performing loans (before foreclosures) to the general public. All the non-performing mortgages will end in a house, an apartment, a store, etc.
Our customers are able to invest from 10,000usd to 1,000,000usd (average 50,000usd).
Our customers' usual focus groups are employees who want second earnings, perceiving the business feeling without outlay time. They look for a solid finance sense corporation that confers them certainty.
Nearly all our clients desire the house, apartment, store, etc. more than the actual earnings.
The name of our company is BRAMLEX
Reason: We value the time and effort you already invest in our project. We realize that we did't come back on some of the doubts requested by the designers. It will be inequitable to the designers who prerequisite our feedback. We also appreciate the comprehension of the community in this postponement.
Reason: Designers,
We really apreciate all the time and effort you put on our project. From the begining we ask for 3 pages, so now we will leave the 10 finalist and provide some extra time to submit the other 2 pages.
We will race the price in 10%
Target Market(s)
Our customers average investors works as employees and want to have a second income or business without spending time. (People from 35 to 50)
Industry/Entity Type
Finance
Requirements
Should not have
- FLASH

```html
<!DOCTYPE html>
<html lang="en">
<head>
<meta charset="utf-8">
<title>Bramlex Remates Hipotecarios</title>
<link rel="stylesheet" href="https://fonts.googleapis.com/css2?family=Barlow+Condensed:wght@400;500;600;700&family=Arimo:wght@400;700&display=swap">
<style>
:root{
  --gold:#b0a83c;
  --olive:#6b6a1f;
  --ink:#1c1c1c;
  --charcoal:#2a2a2a;
  --paper:#f3f2ee;
  --paper-light:#fbfbf9;
  --white:#ffffff;
}
*{margin:0;padding:0;box-sizing:border-box}
html,body{width:1200px;height:758px;overflow:hidden}
body{
  position:relative;
  background:radial-gradient(ellipse at 55% 35%,var(--paper-light) 0%,var(--paper) 70%,#e9e8e3 100%);
  font-family:'Barlow Condensed',sans-serif;
  color:var(--ink);
}
.top-rule{position:absolute;left:0;top:0;width:1200px;height:4px;background:var(--gold)}
.main-nav{position:absolute;left:0;top:0;width:1200px;height:80px}
.nav-home{position:absolute;left:300px;top:4px;width:94px;height:67px}
.nav-home .tab-edge{position:absolute;left:0;top:0;width:14px;height:67px;background:var(--olive)}
.nav-home .tab-shadow{position:absolute;left:14px;top:0;width:80px;height:67px;background:var(--charcoal)}
.nav-home .tab{position:absolute;left:14px;top:0;width:74px;height:62px;background:var(--gold);
  color:var(--white);font-weight:600;font-size:17px;text-align:center;padding-top:21px}
.nav-home svg{position:absolute;left:0;top:67px}
.nav-link{position:absolute;top:23px;font-weight:600;font-size:17px;color:var(--gold);
  text-decoration:none;white-space:nowrap}
.tile{position:absolute;border:4px solid var(--olive)}
.tile.light{border-color:var(--gold)}
.tile-fill{width:100%;height:100%;border:3px solid var(--white)}
.tile-label{position:absolute;height:31px;background:var(--olive);color:var(--ink);
  font-weight:600;font-size:16px;line-height:33px;padding-left:11px;white-space:nowrap}
.tile-label strong{color:var(--white);font-weight:600;font-size:23px}
.tile-label.dark{background:#141414;color:var(--gold)}
.tile-label svg{position:absolute;right:6px;bottom:-9px}
.brand{position:absolute;left:290px;top:478px;width:180px}
.brand-name{font-weight:700;font-size:52px;color:#333;letter-spacing:1px;line-height:1;white-space:nowrap}
.brand-rule{position:absolute;left:0;top:82px;width:178px;height:1px;background:#c9c9c4}
.brand-tag{position:absolute;left:0;top:86px;font-family:'Arimo',sans-serif;font-size:11px;letter-spacing:2.6px;color:#3a3a3a;white-space:nowrap}
.phone{position:absolute;left:310px;top:590px;display:flex;align-items:center;gap:4px;
  font-weight:600;font-size:29px;color:var(--olive);white-space:nowrap}
.divider{position:absolute;left:494px;top:504px;width:1px;height:110px;background:#d4d3cd}
.pitch{position:absolute;left:516px;top:503px;width:430px}
.pitch h1{font-weight:600;font-size:29px;line-height:28px;color:var(--olive);text-transform:uppercase;letter-spacing:-.2px}
.pitch h1 em{font-style:normal;color:var(--ink)}
.pitch p{margin-top:8px;font-weight:600;font-size:14px;color:var(--ink);text-transform:uppercase;white-space:nowrap}
.pitch p span{font-weight:500;color:#3d3d3d}
.search{position:absolute;left:515px;top:592px;display:flex;gap:4px}
.search input{width:214px;height:26px;border:1px solid #d6d6d1;background:var(--white);
  font-family:'Arimo',sans-serif;font-size:8px;color:#999;padding-left:10px}
.search button{width:50px;height:24px;border:none;background:var(--olive);color:var(--white);
  font-family:'Arimo',sans-serif;font-size:9px;box-shadow:3px 3px 0 #4a4a16}
.footer-band{position:absolute;left:0;top:646px;width:1200px;height:15px;background:var(--olive)}
.footer{position:absolute;left:0;top:663px;width:1200px;height:95px;background:var(--gold)}
.footer-nav{position:absolute;left:289px;top:22px;display:flex;font-family:'Arimo',sans-serif;font-weight:700;font-size:7px;white-space:nowrap}
.footer-nav a{color:var(--ink);text-decoration:none;padding:0 5px;border-left:1px solid #8c8530}
.footer-nav a:first-child{padding-left:0;border-left:none}
.legal{position:absolute;left:289px;top:43px;font-family:'Arimo',sans-serif;font-size:7.5px;line-height:9px;color:var(--ink)}
.social{position:absolute;left:821px;top:22px;display:flex;gap:7px}
.social span{width:10px;height:10px;border-radius:50%;background:var(--white)}
</style>
</head>
<body>
<div class="top-rule"></div>

<nav class="main-nav">
  <div class="nav-home">
    <div class="tab-edge"></div>
    <div class="tab-shadow"></div>
    <a class="tab">HOME</a>
    <svg width="22" height="9" viewBox="0 0 22 9"><polygon points="0,0 22,0 11,9" fill="#6b6a1f"/></svg>
  </div>
  <a class="nav-link" style="left:417px">BUYING</a>
  <a class="nav-link" style="left:494px">REFINANCE</a>
  <a class="nav-link" style="left:583px">RENEW COMMERCIAL</a>
  <a class="nav-link" style="left:724px">CONTACT</a>
  <a class="nav-link" style="left:800px">RESOURCES</a>
</nav>

<div class="tile" style="left:486px;top:101px;width:154px;height:107px">
  <div class="tile-fill" role="img" aria-label="Business team meeting around a conference table" style="background:linear-gradient(135deg,#e8e8e6,#b9bcc2 60%,#6d6f75)"></div>
</div>
<div class="tile-label" style="left:486px;top:213px;width:154px">WHAT <strong>WE DO?</strong>
  <svg width="22" height="10" viewBox="0 0 22 10"><polygon points="0,0 22,0 11,10" fill="#6b6a1f"/></svg>
</div>

<div class="tile" style="left:652px;top:101px;width:255px;height:107px">
  <div class="tile-fill" role="img" aria-label="Calculator and pen on a printed financial chart" style="background:linear-gradient(120deg,#d9dcd8,#a8b0ab 45%,#e7c7c0 80%,#d9d9d6)"></div>
</div>
<div class="tile-label" style="left:652px;top:213px;width:255px">MORTGAGE <strong>FINANCIAL ADVICE</strong></div>

<div class="tile light" style="left:652px;top:253px;width:255px;height:185px">
  <div class="tile-fill" role="img" aria-label="Two-storey suburban house with trees and lawn" style="background:linear-gradient(180deg,#cfe0ee 0%,#e6e8e2 40%,#b9ad94 65%,#7d8a52 100%)"></div>
</div>
<div class="tile-label dark" style="left:652px;top:440px;width:255px;height:33px">WELCOME TO <strong>BRAMLEX</strong>
  <svg width="22" height="10" viewBox="0 0 22 10"><polygon points="0,0 22,0 11,10" fill="#141414"/></svg>
</div>

<div class="brand">
  <div class="brand-name">BRAMLEX</div>
  <div class="brand-rule"></div>
  <div class="brand-tag">REMATES HIPOTECARIOS</div>
</div>

<div class="phone">
  <svg width="20" height="20" viewBox="0 0 24 24"><path d="M6.6 10.8a15.1 15.1 0 0 0 6.6 6.6l2.2-2.2a1 1 0 0 1 1-.25 11.4 11.4 0 0 0 3.6.6 1 1 0 0 1 1 1V20a1 1 0 0 1-1 1A17 17 0 0 1 3 4a1 1 0 0 1 1-1h3.5a1 1 0 0 1 1 1c0 1.250.2 2.45.6 3.6a1 1 0 0 1-.25 1z" fill="#1c1c1c"/></svg>
  (555) 214-7730
</div>

<div class="divider"></div>

<section class="pitch">
  <h1>Offering <em>non performing</em> loans to<br>the general public</h1>
  <p>Our customers are able to invest from <span>10,000 USD</span> to <span>1,000,000 USD</span></p>
</section>

<form class="search">
  <input type="text" placeholder="Enter Your Keywords Here.....">
  <button type="button">SEARCH</button>
</form>

<div class="footer-band"></div>
<footer class="footer">
  <nav class="footer-nav">
    <a>BUYING</a><a>REFINANCE</a><a>RENEW COMMERCIAL</a><a>CONTACT</a><a>RESOURCES</a>
  </nav>
  <p class="legal">©2013 &nbsp;Bramlex Remates. Privacy Policy - Terms of Conditions.<br>All Rights Reserved</p>
  <div class="social" aria-label="Social links"><span></span><span></span><span></span><span></span><span></span></div>
</footer>
</body>
</html>
```